Design a Website Mockup for a Clinic

first look at our existing website [url removed, login to view] , this is a clinic website and we want redesign it, we need a professional and simple mockup for it.

```html
<!DOCTYPE html>
<html lang="en">
<head>
<meta charset="utf-8">
<title>Northgate Spine Unit</title>
<link href="https://fonts.googleapis.com/css2?family=Marcellus&display=swap" rel="stylesheet">
<style>
:root{
  --teal:#00a5c4;
  --teal-dark:#0891ad;
  --lime:#a3c13a;
  --white:#ffffff;
  --grey:#7d8a90;
  --line:#cfe6ec;
  --ink:#2b3a40;
  --btn-ink:#12303a;
}
*{margin:0;padding:0;box-sizing:border-box}
html,body{width:711px;height:1200px;overflow:hidden;background:var(--white)}
body{position:relative;font-family:Arial,Helvetica,sans-serif;color:var(--ink)}
.abs{position:absolute}

/* hero */
.hero{left:0;top:0;width:711px;height:333px;
  background:radial-gradient(ellipse at 50% 45%,#f4fbfd 0%,#d6eff5 45%,#8fd0df 80%,#5fb9cc 100%)}
.nav{left:0;top:22px;width:711px;height:32px;background:rgba(255,255,255,.85);border-bottom:1px solid #c9dde3}
.brand{left:109px;top:22px;width:133px;height:32px;background:var(--white);display:flex;align-items:center}
.brand .lime{width:20px;height:32px;background:var(--lime)}
.brand .name{flex:1;text-align:center;font-family:'Marcellus',serif;font-size:7px;color:var(--ink);letter-spacing:.3px}
.brand .tealbar{width:20px;height:32px;background:var(--teal)}
.menu{left:308px;top:33px;display:flex;gap:12px;font-family:'Marcellus',serif;font-size:8.5px;color:var(--teal)}
.taglines{left:0;top:182px;width:711px;text-align:center;font-family:'Marcellus',serif;font-size:10px;letter-spacing:2px;color:var(--teal-dark);line-height:18px}
.pill{top:246px;height:34px;border-radius:17px;background:linear-gradient(#a8e2ee,#6cc8dc);
  box-shadow:0 2px 3px rgba(0,0,0,.18);display:flex;align-items:center;padding-left:4px;
  font-family:'Marcellus',serif;font-size:14px;color:var(--btn-ink)}
.pill .ic{width:26px;height:26px;border-radius:50%;border:2px solid var(--btn-ink);display:flex;align-items:center;justify-content:center;margin-right:6px;background:rgba(255,255,255,.3)}

/* headings */
.title{left:0;width:711px;text-align:center;font-family:'Marcellus',serif;letter-spacing:1.5px}
.more{width:90px;left:310px;text-align:center;font-family:'Marcellus',serif;font-size:7px;letter-spacing:4px;padding-bottom:3px;border-bottom:1px solid}

/* features */
.feature{top:415px;width:86px;text-align:center}
.feature .ring{width:86px;height:86px;border-radius:50%;border:1px solid var(--teal);display:flex;align-items:center;justify-content:center}
.feature .label{margin-top:8px;font-family:'Marcellus',serif;font-size:6.5px;color:var(--teal);letter-spacing:.6px}

/* team */
.band-team{left:0;top:543px;width:711px;height:200px}
.card{top:616px;width:123px;height:128px;background:var(--white);padding:3px;box-shadow:0 1px 3px rgba(0,0,0,.25)}
.card .photo{width:117px;height:122px;background:linear-gradient(#e9ecef,#9aa7b0);position:relative}
.card .cap{position:absolute;left:0;bottom:0;width:117px;height:26px;background:var(--teal);color:var(--white);padding:4px 6px 0}
.card .cap b{display:block;font-weight:normal;font-size:7.5px;line-height:10px;white-space:nowrap}
.card .cap span{display:block;font-size:4.8px;line-height:7px;white-space:nowrap}
.team-note{left:0;top:758px;width:711px;text-align:center;font-size:6px;color:var(--teal);line-height:7.5px}

/* testimonials */
.quote{left:131px;top:864px;width:258px;font-size:7.5px;color:var(--white);line-height:18px}
.author{left:132px;top:917px;font-size:11px;font-weight:bold;color:var(--white)}
.date{left:133px;top:932px;font-size:5px;color:var(--white)}

/* booking */
.book{left:260px;top:980px;width:183px;height:33px;border-radius:17px;background:linear-gradient(#a8e2ee,#6cc8dc);
  box-shadow:0 2px 3px rgba(0,0,0,.18);display:flex;align-items:center;padding-left:6px;font-family:'Marcellus',serif;font-size:13px;color:var(--btn-ink)}
.book .ic{width:25px;height:25px;border-radius:50%;border:2px solid var(--btn-ink);display:flex;align-items:center;justify-content:center;margin-right:8px;background:rgba(255,255,255,.3)}
.social{top:1025px;width:28px;height:28px;border-radius:50%;border:2px solid var(--teal);
  display:flex;align-items:center;justify-content:center;font-family:'Marcellus',serif;font-size:6px;color:var(--teal)}

/* footer */
.rule{left:119px;width:464px;height:1px;background:var(--line)}
.fcol{top:1084px}
.fcol h4{font-family:'Marcellus',serif;font-weight:normal;font-size:9.5px;color:var(--teal);letter-spacing:.8px;margin-bottom:4px}
.fcol p{font-size:5px;color:var(--grey);line-height:9.8px}
.copy{left:121px;top:1183px;font-size:5px;color:var(--grey)}
</style>
</head>
<body>

<!-- hero -->
<div class="abs hero" role="img" aria-label="Photo: surgical team in masks and caps looking down at the patient"></div>
<div class="abs nav"></div>
<div class="abs brand"><div class="lime"></div><div class="name">NORTHGATE SPINE UNIT</div><div class="tealbar"></div></div>
<nav class="abs menu"><span>HOME</span><span>FOR PATIENTS</span><span>ABOUT US</span><span>ARTICLES</span><span>TESTIMONIALS</span></nav>
<div class="abs taglines">PHYSICAL THERAPY<br>PAIN MANAGEMENT<br>SPINAL SURGERY</div>
<div class="abs pill" style="left:200px;width:147px">
  <span class="ic"><svg width="14" height="14" viewBox="0 0 24 24"><path fill="#12303a" d="M6.6 10.8a15.1 15.1 0 0 0 6.6 6.6l2.2-2.2c.3-.3.7-.4 1-.2 1.1.4 2.3.6 3.6.6.6 0 1 .4 1 1V20c0 .6-.4 1-1 1A17 17 0 0 1 3 4c0-.6.4-1 1-1h3.5c.6 0 1 .4 1 1 0 1.3.2 2.5.6 3.6.1.3 0 .7-.2 1z"/></svg></span>0800 246 1357</div>
<div class="abs pill" style="left:361px;width:146px">
  <span class="ic"><svg width="14" height="14" viewBox="0 0 24 24"><rect x="6" y="3" width="12" height="5" fill="#12303a"/><rect x="3" y="9" width="18" height="8" rx="2" fill="#12303a"/><rect x="7" y="14" width="10" height="7" fill="#fff" stroke="#12303a" stroke-width="1.5"/></svg></span>0800 246 1358</div>

<!-- approach -->
<div class="abs title" style="top:362px;font-size:11.5px;color:var(--teal)">COMPREHENSIVE SPINE CARE WITH A MULTIDISCIPLINARY APPROACH</div>
<div class="abs more" style="top:386px;color:var(--teal);border-color:var(--teal)">READ ALL</div>

<div class="abs feature" style="left:120px"><div class="ring">
  <svg width="44" height="48" viewBox="0 0 44 48"><rect x="5" y="4" width="32" height="36" rx="4" fill="none" stroke="#00a5c4" stroke-width="3"/><path d="M19 20v16l-4-3-3 2 8 10h12l3-12-8-3v-10z" fill="#00a5c4"/><path d="M15 14a6 6 0 0 1 8 0M13 11a9 9 0 0 1 12 0" stroke="#00a5c4" stroke-width="1.5" fill="none"/></svg>
  </div><div class="label">LATEST TECHNOLOGY</div></div>
<div class="abs feature" style="left:238px"><div class="ring">
  <svg width="64" height="34" viewBox="0 0 64 34"><path d="M2 6l12-4 8 6h10l-8 10 14 8-4 4-20-6L2 20z" fill="#00a5c4"/><path d="M62 6L50 2l-10 4-10 8 6 4 8-4 10 4 8-2z" fill="#00a5c4"/></svg>
  </div><div class="label">COMITMENT</div></div>
<div class="abs feature" style="left:356px"><div class="ring">
  <svg width="56" height="56" viewBox="0 0 56 56"><circle cx="28" cy="7" r="5" fill="#00a5c4"/><circle cx="28" cy="49" r="5" fill="#00a5c4"/><circle cx="7" cy="28" r="5" fill="#00a5c4"/><circle cx="49" cy="28" r="5" fill="#00a5c4"/><path d="M28 14l14 14-14 14-14-14z" fill="#00a5c4"/><path d="M28 12v32M12 28h32" stroke="#fff" stroke-width="2"/></svg>
  </div><div class="label">TEAM SUPPORT</div></div>
<div class="abs feature" style="left:480px"><div class="ring">
  <svg width="40" height="50" viewBox="0 0 40 50"><path d="M12 26l-6 20 7-4 4 6 3-18zM28 26l6 20-7-4-4 6-3-18z" fill="#00a5c4"/><circle cx="20" cy="18" r="16" fill="#00a5c4"/><circle cx="20" cy="18" r="9" fill="none" stroke="#fff" stroke-width="2.5"/></svg>
  </div><div class="label">CIRTIFIED</div></div>

<!-- team -->
<svg class="abs band-team" viewBox="0 0 711 200" preserveAspectRatio="none"><path d="M0 0H711V180L0 195z" fill="var(--lime)"/></svg>
<div class="abs title" style="top:563px;font-size:14px;color:var(--white)">MEET OUR TEAM</div>
<div class="abs more" style="top:585px;color:var(--white);border-color:var(--white)">VIEW ALL</div>

<div class="abs card" style="left:119px"><div class="photo" role="img" aria-label="Portrait of consultant spinal surgeon">
  <div class="cap"><b>MR DEV SHARMA</b><span>MBBS BSC (HONS) MD FRCS (ORTH)</span></div></div></div>
<div class="abs card" style="left:290px"><div class="photo" role="img" aria-label="Portrait of consultant orthopaedic surgeon">
  <div class="cap"><b>MR TUNDE OKORO</b><span>MBBS, FRCSI, FRCS(ORTH)</span></div></div></div>
<div class="abs card" style="left:458px"><div class="photo" role="img" aria-label="Portrait of clinical specialist">
  <div class="cap"><b>MARTIN HALE</b><span>BSC (HONS) BIOLOGY</span></div></div></div>
<div class="abs team-note">Quisque nulla. Vestibulum libero nisl, porta vel, scelerisque eget, malesuada at, neque.<br>Vivamus eget nibh. Etiam cursus leo vel metus</div>

<!-- testimonials -->
<svg class="abs" style="left:0;top:785px" width="711" height="195" viewBox="0 0 711 195"><path d="M0 0H711V193L0 173z" fill="var(--teal)"/>
  <path d="M452 93h45v36l-20 45h-22l15-40h-18z M528 93h45v36l-20 45h-22l15-40h-18z" fill="#eef3f4"/></svg>
<div class="abs title" style="top:801px;font-size:14px;color:var(--white)">CLIENT TESTIMONIALS</div>
<div class="abs more" style="top:823px;color:var(--white);border-color:var(--white)">VIEW ALL</div>
<p class="abs quote">Mr Sharma was able to see the distress I was in from the moment I walked into the consulting room. The procedure was 100% successful and pain-free. Following some physiotherapy I am back to normal</p>
<div class="abs author">James R</div>
<div class="abs date">March 18, 2013</div>

<!-- booking -->
<div class="abs book"><span class="ic"><svg width="14" height="14" viewBox="0 0 24 24"><rect x="2" y="4" width="16" height="15" rx="1" fill="none" stroke="#12303a" stroke-width="2"/><path d="M2 9h16M6 2v4M14 2v4" stroke="#12303a" stroke-width="2"/><circle cx="17" cy="17" r="5" fill="#fff" stroke="#12303a" stroke-width="2"/><path d="M17 14.5V17h2" stroke="#12303a" stroke-width="1.5" fill="none"/></svg></span>BOOK APPOINTMENT</div>
<div class="abs social" style="left:280px">Feed</div>
<div class="abs social" style="left:319px">Chat</div>
<div class="abs social" style="left:357px">Post</div>
<div class="abs social" style="left:395px">Link</div>

<!-- footer -->
<div class="abs rule" style="top:1071px"></div>
<div class="abs fcol" style="left:122px"><h4>ABOUT</h4><p>Information<br>Appointments<br>What We Do<br>Our Team</p></div>
<div class="abs fcol" style="left:192px"><h4>ARTICLES</h4><p>Spine Conditions<br>Physical Therapy<br>Back Pain<br>Neck Pain<br>Degenerative Spinal Conditions<br>Osteoporotic Spinal Fractures</p></div>
<div class="abs fcol" style="left:301px"><h4>ARTICLES</h4><p>Minimally Invasive Spinal Surgery<br>Spinal Infections<br>Spinal Injections<br>Spinal Trauma<br>Spinal tumours<br>More Topics</p></div>
<div class="abs fcol" style="left:417px"><h4>CONTACT</h4><p>Dr D Sharma MD<br>Riverside Hospital of St Anne<br>14 Elm Park Road<br>Westfield<br>London<br>NW1 4QA<br>Phone : 0800 246 1357</p></div>
<div class="abs rule" style="top:1175px"></div>
<div class="abs copy">© 2015 Northgate Spine Clinic Unit.</div>

</body>
</html>
```